Executive Summary

Create a one page executive summary of a venture fund - with the information here:
https://files.brindlecove.net/d/7qTm3VxR9pLw2KcYhN8sD4fBzJ6gA1eUoXiM5tQrWnE/view?share=open

```html
<!DOCTYPE html>
<html lang="en">
<head>
<meta charset="utf-8">
<title>Ostrivane Decarbonization Partnership Fund – Executive Summary</title>
<link rel="stylesheet" href="https://fonts.googleapis.com/css2?family=Montserrat:wght@700;800&family=Poppins:wght@400;500&display=swap">
<style>
  :root{
    --green:#185b52;
    --navy:#17345c;
    --pale:#e6eef8;
    --white:#ffffff;
    --ink:#1b2b40;
    --photo-a:#c9ccd2;
    --photo-b:#8e9096;
  }
  *{box-sizing:border-box;margin:0;padding:0}
  html,body{width:848px;height:1200px;overflow:hidden;background:var(--white)}
  .sheet{position:relative;width:848px;height:1200px;font-family:"Poppins",sans-serif;color:var(--ink)}
  .block{position:absolute}
  .heading{font-family:"Montserrat",sans-serif;font-weight:800}

  .title-panel{left:0;top:0;width:388px;height:153px;background:var(--green);color:var(--white);
    display:flex;align-items:center;justify-content:center;text-align:center;font-size:28px;line-height:33px;letter-spacing:.3px}
  .tagline-panel{left:388px;top:0;width:460px;height:153px;background:var(--navy);color:var(--white);
    display:flex;align-items:center;justify-content:center;text-align:center;font-size:23px;line-height:32px;font-weight:400}

  .focus-panel{left:0;top:153px;width:848px;height:320px;background:var(--pale)}
  .focus-title{left:30px;top:170px;width:380px;text-align:center;color:var(--navy);font-size:26px;line-height:31px;font-weight:800}

  .pillars{left:462px;top:180px;width:386px}
  .pillar{display:flex;gap:12px;height:90px}
  .pillar svg{flex:0 0 46px;height:46px;margin-top:2px}
  .pillar h3{font-family:"Montserrat",sans-serif;font-weight:800;color:var(--navy);font-size:20px;line-height:24px}
  .pillar p{font-size:15.6px;line-height:20px;color:var(--ink);margin-top:2px;width:320px}

  .terms-panel{left:0;top:299px;width:440px;height:266px;background:var(--navy);color:var(--white);padding:21px 0 0 17px}
  .terms-panel li{list-style:none;font-size:16px;line-height:27.4px}
  .overview-panel{left:440px;top:473px;width:408px;height:92px;background:var(--navy);color:var(--white);
    display:flex;align-items:center;justify-content:center;font-size:29px;padding-left:2px}

  .team-title{left:21px;top:578px;font-size:32px;color:var(--navy)}
  .member{position:absolute;width:210px}
  .photo{display:block;width:181px;height:135px;background:linear-gradient(160deg,var(--photo-a),var(--photo-b))}
  .member h4{font-family:"Montserrat",sans-serif;font-weight:800;color:var(--navy);font-size:16px;line-height:20px;margin-top:12px}
  .member p{font-size:15px;line-height:20px;color:var(--ink)}

  .startups-panel{left:453px;top:874px;width:395px;height:326px;background:var(--green);color:var(--white);padding:24px 20px 0 21px}
  .startups-panel h2{font-family:"Montserrat",sans-serif;font-weight:800;font-size:20px;margin-left:4px;margin-bottom:12px}
  .startups-panel p{font-size:15px;line-height:19.7px}
  .startups-band{left:0;top:1121px;width:453px;height:79px;background:var(--green);color:var(--white);
    display:flex;align-items:center;justify-content:center;font-size:29px}
</style>
</head>
<body>
<main class="sheet">
  <header>
    <div class="block title-panel heading">OSTRIVANE<br>DECARBONIZATION<br>PARTNERSHIP FUND</div>
    <div class="block tagline-panel">Designed for Corporate<br>Decarbonization Partnerships,<br>Presented by Ostrivane Capital</div>
  </header>

  <section>
    <div class="block focus-panel"></div>
    <h1 class="block focus-title heading">Investing in Early<br>Stage Decarbonization<br>Startup companies</h1>

    <div class="block pillars">
      <div class="pillar">
        <svg viewBox="0 0 46 46" aria-hidden="true"><g fill="#185b52"><rect x="8" y="14" width="24" height="18" rx="6" transform="rotate(-35 20 23)"/><rect x="2" y="28" width="12" height="8" rx="2" transform="rotate(-35 8 32)"/><rect x="30" y="12" width="12" height="8" rx="2" transform="rotate(-35 36 16)"/></g></svg>
        <div><h3>Collaboration</h3><p>Corporate LP networkcollaborate on Deals, Insights, Co-investment, and Exits</p></div>
      </div>
      <div class="pillar">
        <svg viewBox="0 0 46 46" aria-hidden="true"><g fill="#185b52"><circle cx="23" cy="20" r="10"/><rect x="18" y="28" width="10" height="8" rx="2"/><rect x="20" y="37" width="6" height="3" rx="1"/></g><g stroke="#185b52" stroke-width="2.5" stroke-linecap="round"><line x1="23" y1="2" x2="23" y2="6"/><line x1="4" y1="20" x2="8" y2="20"/><line x1="38" y1="20" x2="42" y2="20"/><line x1="9" y1="7" x2="12" y2="10"/><line x1="37" y1="7" x2="34" y2="10"/><line x1="9" y1="33" x2="12" y2="30"/><line x1="37" y1="33" x2="34" y2="30"/></g></svg>
        <div><h3>Alpha</h3><p>Next Generation of Solutions Strategic &amp; financial returns</p></div>
      </div>
      <div class="pillar">
        <svg viewBox="0 0 46 46" aria-hidden="true"><g fill="none" stroke="#185b52" stroke-width="4"><circle cx="23" cy="25" r="15"/><circle cx="23" cy="25" r="7"/></g><line x1="23" y1="25" x2="9" y2="11" stroke="#185b52" stroke-width="3" stroke-linecap="round"/><circle cx="23" cy="25" r="2.5" fill="#185b52"/></svg>
        <div><h3>Impact</h3><p>≥2 Gt CO₂e reduction potential per portfolio reduced by 2050</p></div>
      </div>
    </div>

    <ul class="block terms-panel">
      <li>Fund Size: $100M</li>
      <li>Term: 10+1+1 Years</li>
      <li>Stage: Pre-seed - Series B (Seed / Series A focus)</li>
      <li>Target Returns: 3x of Invested Capital / 15%-25% IRR</li>
      <li>Portfolio Number: 30</li>
      <li>Check Size: $0.25M - $5M (stage-dependent)</li>
      <li>Follow-on Reserve: 50%</li>
      <li>Geography: N.A, Asia, Europe</li>
    </ul>
    <h2 class="block overview-panel heading">Fund Term Overview</h2>
  </section>

  <section>
    <h2 class="block team-title heading">Team</h2>

    <div class="member" style="left:25px;top:635px">
      <div class="photo" role="img" aria-label="Portrait photo of Lin (Laura) Park"></div>
      <h4>Lin (Laura) Park</h4><p>Managing Partner</p>
    </div>
    <div class="member" style="left:224px;top:635px">
      <div class="photo" role="img" aria-label="Portrait photo of Suda Rattanakornwong" style="margin-left:6px"></div>
      <h4>Suda<br>Rattanakornwong,</h4><p>Venture Partner</p>
    </div>
    <div class="member" style="left:436px;top:635px">
      <div class="photo" role="img" aria-label="Portrait photo of Daniel Cho" style="background:linear-gradient(160deg,#3f6a33,#caa089)"></div>
      <h4>Daniel Cho, PhD</h4><p>Venture Partner<br>(New York)</p>
    </div>
    <div class="member" style="left:636px;top:635px">
      <div class="photo" role="img" aria-label="Portrait photo of Mia Tan" style="background:linear-gradient(160deg,#f4f4f4,#d8b6a0)"></div>
      <h4>Mia Tan, CFA</h4><p>&nbsp;Vice President<br>(California):</p>
    </div>
    <div class="member" style="left:25px;top:869px">
      <div class="photo" role="img" aria-label="Portrait photo of Grace Lim" style="background:linear-gradient(160deg,#6e6e6e,#3a3a3a)"></div>
      <h4 style="margin-top:20px">Grace Lim</h4><p>Chef of Staff<br>(California):</p>
    </div>
    <div class="member" style="left:224px;top:869px;width:230px">
      <div class="photo" role="img" aria-label="Portrait photo of Evan Holloway" style="margin-left:6px;background:linear-gradient(160deg,#6f6f6f,#2c3344)"></div>
      <h4 style="margin-top:20px">Evan Holloway, J.D.<br>Legal Advisor (New York):</h4><p>Senior Counsel at Corvane<br>Ventures,</p>
    </div>
  </section>

  <section>
    <div class="block startups-panel">
      <h2>Example Portfolio Startups</h2>
      <p>The Northgate Tech Spin out company has developed a proprietary process to synthesize commodity chemicals, starting with green methanol and ammonia, at cost-parity using used diesel engines. By converting these engines to consume inputs such as methane, biogas, and carbon dioxide, the company has created a low-carbon process to produce these chemicals by displacing the need for flaring or release of methane, plugging into waste streams offsite.</p>
    </div>
    <h2 class="block startups-band heading">Example Portfolio Startups</h2>
  </section>
</main>
</body>
</html>
```